Vintage Packaging Needed for Vintage Sports Equipment
We have 5 different boxes which require a similar packaging design. We have uploaded the design templates and logo.
Initially, please focus on the soccer ball first. Our products are vintage sports equipment that come with very nice wooden display mounts. The sport equipment can be played with or can be used as a display piece.
The logo color can be altered. We have not identified a brand color yet. We desire the branding and packaging to represent high quality vintage sport equipment. Many of the designs come from the early 1920s or earlier.
The products come in real leather or faux leather.
Example styles attached.
Target Market(s)
Youth, Adults, Business Offices - products used as desk pieces for show etc,
Requirements
Must have
- Must have company Logo.
- Must have placeholder for Bar Code
- Must have following text:
- Distributed By:
- Marrowfen Goods, LLC
- 5871 W Quarry Ln
- #417
- Provo, UT 84612
- MADE IN INDIA WITH GLOBALLY SOURCED MATERIALS
- Marrowfen and Tidal Relic are trademarks of Marrowfen Goods, LLC.
- © 2017, Marrowfen Goods, LLC. All rights reserved.
- Name of Sport Equipment in Package (Basketball, Soccer ball, etc)
- (warranty is preferably on the bottom of the packaging)
- Warranty
- MARROWFEN, warrants this product against defects in materials and workmanship under normal use for a period of ONE (1) YEAR from the date of retail purchase by the original end-user purchaser (“Warranty Period”). MARROWFEN MAKES NO OTHER WARRANTIES, EXPRESS OR IMPLIED, INCLUDING BU NOT LIMITED TO THE WARRANTIES OF MERCHANTABILITY OR FITNESS FOR A PARTICULAR PURPOSE. Original receipt required to validate warranty and all claims are subject to approval by MARROWFEN. MARROWFEN WILL NOT BE LIABLE FOR ANY SPECIAL, INCIDENTAL, OR CONSEQUENTIAL DAMAGES. MARROWFEN's liability with respect to a claim for any damages arising out of or connected with the sale, manufacture, use, inability to use, or performance of this product will be limited to replacement of the product only. Purchases should independently determine the suitability of each material for the specific purpose prior to use.
- We also need these in AI and PSD file formats.
Nice to have
- We'd like designers to take some liberty and add other elements as they see fit based on creativity or past experience in packaging.
- Website address of designer

```html
<!DOCTYPE html>
<html lang="en">
<head>
<meta charset="utf-8">
<title>Tidal Relic – Soccer Ball Box Dieline</title>
<link rel="stylesheet" href="https://fonts.googleapis.com/css2?family=Marcellus&family=Audiowide&family=Arimo:wght@400;700&display=swap">
<style>
  :root {
    --paper: #ffffff;
    --panel: #c9cac1;
    --navy: #29295a;
    --cream: #f3ede2;
    --edge: #e4d6cd;
    --dieline: #c4c4c4;
    --ink: #2b2b3a;
  }
  html, body {
    margin: 0;
    width: 1200px;
    height: 818px;
    overflow: hidden;
    background: var(--paper);
  }
  .sheet {
    position: relative;
    width: 1500px;
    height: 1023px;
    transform: scale(0.8);
    transform-origin: 0 0;
  }
  .dieline-art { position: absolute; inset: 0; }
  .serif { font-family: "Marcellus", Georgia, serif; }
  .display { font-family: "Audiowide", "Arial Black", sans-serif; }

  .side-copy {
    position: absolute;
    left: 503px;
    top: 505px;
    width: 204px;
    font-family: "Arimo", Arial, sans-serif;
    font-size: 6.2px;
    line-height: 7.3px;
    color: var(--ink);
    text-align: justify;
  }
  .side-copy p { margin: 0 0 8px; }

  .distributor {
    position: absolute;
    left: 480px;
    top: 628px;
    width: 250px;
    text-align: center;
    font-family: "Arimo", Arial, sans-serif;
    font-size: 8px;
    line-height: 9.6px;
    color: var(--ink);
  }
  .barcode-slot {
    position: absolute;
    left: 557px;
    top: 667px;
    width: 96px;
    height: 42px;
    background: #ffffff;
  }

  .brand-mark {
    position: absolute;
    left: 1232px;
    top: 496px;
    width: 150px;
    text-align: center;
    color: var(--ink);
  }
  .brand-mark .brand-name {
    font-family: "Marcellus", Georgia, serif;
    font-size: 10px;
    letter-spacing: 0.5px;
    padding-bottom: 2px;
    border-bottom: 1px solid var(--ink);
    display: inline-block;
  }
  .brand-mark .product-name {
    margin-top: 16px;
    font-family: "Marcellus", Georgia, serif;
    font-size: 5.5px;
    letter-spacing: 2.5px;
  }

  .legal {
    position: absolute;
    left: 1213px;
    top: 558px;
    width: 193px;
    font-family: "Arimo", Arial, sans-serif;
    font-size: 5.6px;
    line-height: 6.2px;
    color: var(--ink);
  }
  .legal .origin {
    text-align: center;
    font-size: 7.2px;
    line-height: 8.6px;
    margin: 0 0 7px;
  }
  .legal .trademark { margin: 0 0 12px; }
  .legal .warranty-title { margin: 0; }
  .legal .warranty-text { margin: 0; text-align: justify; }
</style>
</head>
<body>
<div class="sheet">
  <svg class="dieline-art" width="1500" height="1023" viewBox="0 0 1500 1023" xmlns="http://www.w3.org/2000/svg">
    <defs>
      <pattern id="dot-track" x="79" y="0" width="8" height="1023" patternUnits="userSpaceOnUse">
        <rect x="1" y="745.5" width="5" height="5" fill="var(--navy)"/>
      </pattern>
      <clipPath id="lid-clip"><rect x="781" y="80" width="351" height="350"/></clipPath>

      <g id="display-face">
        <rect x="0" y="430" width="351" height="355" fill="var(--panel)"/>
        <rect x="0" y="430" width="351" height="4" fill="var(--edge)"/>
        <rect x="0" y="781" width="351" height="4" fill="var(--edge)"/>
        <g class="label-rule" stroke="var(--navy)" stroke-width="2.5">
          <line x1="0" y1="471" x2="111" y2="471"/>
          <line x1="239" y1="471" x2="351" y2="471"/>
        </g>
        <rect class="label-box" x="111" y="452" width="128" height="39" fill="var(--navy)"/>
        <rect x="115" y="456" width="120" height="31" fill="none" stroke="var(--cream)" stroke-width="2"/>
        <g class="stripes" stroke="var(--navy)" stroke-width="2.5">
          <line x1="0" y1="559" x2="351" y2="559"/>
          <line x1="0" y1="571.5" x2="351" y2="571.5"/>
          <line x1="0" y1="584" x2="351" y2="584"/>
          <line x1="0" y1="596.5" x2="351" y2="596.5"/>
          <line x1="0" y1="609" x2="351" y2="609"/>
          <line x1="0" y1="621.5" x2="351" y2="621.5"/>
          <line x1="0" y1="634" x2="351" y2="634"/>
          <line x1="0" y1="646.5" x2="351" y2="646.5"/>
        </g>
        <path id="badge" d="M176,507 L276,557 Q319,578 319,597 Q319,616 276,637 L176,687 L76,637 Q33,616 33,597 Q33,578 76,557 Z"
              fill="var(--navy)" stroke="var(--navy)" stroke-width="14" stroke-linejoin="round"/>
        <use href="#badge" fill="none" stroke="var(--cream)" stroke-width="8"/>
        <path d="M176,507 L276,557 Q319,578 319,597 Q319,616 276,637 L176,687 L76,637 Q33,616 33,597 Q33,578 76,557 Z" fill="var(--navy)"/>
        <text class="serif" x="176" y="613" text-anchor="middle" font-size="21" letter-spacing="1" fill="var(--cream)">TIDAL RELIC</text>
        <line x1="106" y1="621" x2="246" y2="621" stroke="var(--cream)" stroke-width="1"/>
        <text class="display" x="176" y="729" text-anchor="middle" font-size="16" letter-spacing="3.2" fill="var(--navy)">CHOICE OF THE CHAMPIONS</text>
        <rect x="0" y="741.5" width="351" height="2.5" fill="var(--navy)"/>
        <rect x="0" y="745.5" width="351" height="5" fill="url(#dot-track)"/>
        <rect x="0" y="752" width="351" height="2.5" fill="var(--navy)"/>
      </g>
    </defs>

    <!-- wrap band -->
    <rect class="wrap-band" x="79" y="430" width="1403" height="355" fill="var(--panel)"/>
    <rect x="79" y="430" width="1403" height="4" fill="var(--edge)"/>
    <rect x="79" y="781" width="1403" height="4" fill="var(--edge)"/>
    <rect x="79" y="741.5" width="1403" height="2.5" fill="var(--navy)"/>
    <rect x="79" y="745.5" width="1403" height="5" fill="url(#dot-track)"/>
    <rect x="79" y="752" width="1403" height="2.5" fill="var(--navy)"/>

    <!-- printed faces -->
    <use href="#display-face" x="79"/>
    <use href="#display-face" x="781"/>
    <g class="lid-face" clip-path="url(#lid-clip)">
      <rect x="781" y="78" width="351" height="352" fill="var(--panel)"/>
      <g transform="rotate(180 956.5 255.75) translate(781 -352.5)">
        <use href="#display-face"/>
      </g>
      <rect x="781" y="78" width="351" height="4" fill="var(--edge)"/>
    </g>

    <!-- fold lines -->
    <g class="folds" stroke="#d8d6d0" stroke-width="1">
      <line x1="430" y1="430" x2="430" y2="785"/>
      <line x1="781" y1="430" x2="781" y2="785"/>
      <line x1="1132" y1="430" x2="1132" y2="785"/>
    </g>

    <!-- cut lines -->
    <g class="cut-lines" fill="none" stroke="var(--dieline)" stroke-width="1.2">
      <path d="M79,430 L18,470 L18,748 L79,785"/>
      <path d="M208,430 L208,393 Q208,378 223,378 L285,378 Q300,378 300,393 L300,430"/>
      <path d="M430,430 L430,118 L494,118 L494,252 L781,252"/>
      <path d="M781,430 L781,40 Q781,18 803,18 L1110,18 Q1132,18 1132,40 L1132,430"/>
      <path d="M1132,252 L1418,252 L1418,118 L1482,118 L1482,430"/>
      <path d="M79,785 L170,972 L172,1030 L338,1030 L340,972 L430,785"/>
      <path d="M430,785 L430,905 L655,905 L605,853 L700,853 L781,785"/>
      <path d="M781,785 L781,1023 M1132,785 L1132,1023"/>
      <path d="M852,1023 L852,985 L866,950 L1050,950 L1064,985 L1064,1023"/>
      <path d="M1132,785 L1212,853 L1308,853 L1258,905 L1482,905 L1482,785"/>
    </g>

    <!-- crop marks -->
    <g class="crop-marks" stroke="#555" stroke-width="1">
      <line x1="430" y1="0" x2="430" y2="15"/>
      <line x1="781" y1="0" x2="781" y2="15"/>
      <line x1="1132" y1="0" x2="1132" y2="15"/>
      <line x1="0" y1="78" x2="15" y2="78"/>
      <line x1="0" y1="430" x2="15" y2="430"/>
      <line x1="0" y1="785" x2="15" y2="785"/>
      <line x1="1485" y1="78" x2="1500" y2="78"/>
      <line x1="1485" y1="430" x2="1500" y2="430"/>
      <line x1="1485" y1="785" x2="1500" y2="785"/>
      <line x1="430" y1="1008" x2="430" y2="1023"/>
      <line x1="1482" y1="1008" x2="1482" y2="1023"/>
    </g>
  </svg>

  <!-- side panel copy -->
  <div class="side-copy">
    <p>Every piece in this collection is crafted to echo the early days of sport, when balls were stitched by hand from thick leather panels. Each ball arrives with a solid wooden display mount, ready for the field or a place of honour on your desk, shelf or office table. Real and faux leather options share the same careful stitching, weighted feel and warm aged finish that collectors love. Play with it, display it, and let it tell a story.</p>
    <p>Inside the box you will find one vintage style soccer ball, one wooden display mount and a care card. Wipe the leather with a soft dry cloth and keep it away from direct heat and strong sunlight. Store indoors when not in use so the finish ages slowly and evenly over the years.</p>
  </div>
  <div class="distributor">
    Distributed By:<br>
    Marrowfen Goods, LLC<br>
    5871 W Quarry Ln #417 Provo, UT 84612
  </div>
  <div class="barcode-slot" aria-label="Barcode placeholder"></div>

  <!-- back panel -->
  <div class="brand-mark">
    <span class="brand-name">TIDAL RELIC</span>
    <div class="product-name">SOCCER BALL</div>
  </div>
  <div class="legal">
    <p class="origin">MADE IN INDIA<br>WITH GLOBALLY SOURCED MATERIALS</p>
    <p class="trademark">Marrowfen and Tidal Relic are trademarks of Marrowfen Goods, LLC.<br>© 2017, Marrowfen Goods, LLC. All rights reserved.<br>Name of Sport Equipment in Package (Basketball, Soccer ball, etc)</p>
    <p class="warranty-title">WARRANTY</p>
    <p class="warranty-text">MARROWFEN, warrants this product against defects in materials and workmanship under normal use for a period of ONE (1) YEAR from the date of retail purchase by the original end-user purchaser (“Warranty Period”). MARROWFEN MAKES NO OTHER WARRANTIES, EXPRESS OR IMPLIED, INCLUDING BU NOT LIMITED TO THE WARRANTIES OF MERCHANTABILITY OR FITNESS FOR A PARTICULAR PURPOSE. Original receipt required to validate warranty and all claims are subject to approval by MARROWFEN. MARROWFEN WILL NOT BE LIABLE FOR ANY SPECIAL, INCIDENTAL, OR CONSEQUENTIAL DAMAGES. MARROWFEN's liability with respect to a claim for any damages arising out of or connected with the sale, manufacture, use, inability to use, or performance of this product will be limited to replacement of the product only. Purchases should independently determine the suitability of each material for the specific purpose prior to use.</p>
  </div>
</div>
</body>
</html>
```